- Redesign our business card
- Logo remains unchanged
- Current business card attached

Target Market(s)

We are a property management company

Industry/Entity Type

Business

```html
<!DOCTYPE html>
<html lang="en">
<head>
<meta charset="utf-8">
<title>Kestrel Property Group – Business Card</title>
<link rel="stylesheet" href="https://fonts.googleapis.com/css2?family=Roboto+Condensed:wght@400;700&display=swap">
<style>
  :root {
    --stage-light: #4b601f;
    --stage-dark: #1d1a17;
    --olive: #6f7a3f;
    --charcoal: #5b5959;
    --ink: #222222;
    --text: #3a3a3a;
    --sand: #d1c49b;
    --white: #ffffff;
  }
  * { margin: 0; padding: 0; box-sizing: border-box; }
  html, body { width: 1200px; height: 1200px; overflow: hidden; }
  body {
    position: relative;
    background: linear-gradient(135deg, var(--stage-light) 0%, #2f3419 45%, var(--stage-dark) 75%);
    font-family: "Roboto Condensed", "Arial Narrow", sans-serif;
  }
  .card {
    position: absolute;
    width: 795px;
    height: 440px;
    border-radius: 30px;
    overflow: hidden;
  }
  .card-front { left: 72px; top: 142px; background: var(--white); }
  .card-back { left: 333px; top: 615px; background: var(--sand); }

  .brand { position: absolute; }
  .brand-name {
    display: flex; align-items: center; gap: 10px;
    font-weight: 700; color: var(--olive); letter-spacing: 0.3px; white-space: nowrap;
  }
  .brand-mark { display: inline-block; background: var(--olive); }
  .brand-tagline { color: var(--charcoal); letter-spacing: 0.4px; white-space: nowrap; }

  .card-front .brand { left: 60px; top: 168px; }
  .card-front .brand-name { font-size: 19px; }
  .card-front .brand-mark { width: 16px; height: 16px; }
  .card-front .brand-tagline { font-size: 12.5px; margin-top: 3px; padding-left: 26px; }

  .person { position: absolute; left: 362px; top: 68px; }
  .person-name { font-size: 25px; font-weight: 700; color: var(--ink); }
  .person-title { font-size: 16px; color: var(--text); margin-top: 2px; }

  .address { position: absolute; left: 362px; top: 190px; font-size: 18px; line-height: 25px; color: var(--text); }

  .contacts { position: absolute; left: 362px; top: 262px; list-style: none; font-size: 18px; color: var(--text); }
  .contacts li { display: flex; align-items: center; height: 25.5px; }
  .contact-icon {
    width: 15px; height: 15px; margin-right: 20px;
    background: var(--olive); color: var(--white);
    font-size: 10px; font-weight: 700; line-height: 15px; text-align: right; padding-right: 1px;
  }

  .services-band {
    position: absolute; left: 0; bottom: 0; width: 100%; height: 52px;
    background: var(--olive); color: var(--white);
    display: flex; align-items: center; justify-content: center;
    font-size: 18.5px; font-weight: 700; letter-spacing: 0.2px;
  }
  .services-band .divider { margin: 0 12px; }

  .card-back .brand { left: 248px; top: 244px; }
  .card-back .brand-name { font-size: 23px; }
  .card-back .brand-mark { width: 20px; height: 20px; }
  .card-back .brand-tagline { font-size: 16px; margin-top: 4px; padding-left: 30px; }
  .website { position: absolute; left: 248px; top: 362px; font-size: 23px; font-weight: 700; color: var(--olive); }
</style>
</head>
<body>
  <section class="card card-front">
    <div class="brand">
      <div class="brand-name"><span class="brand-mark"></span>KESTREL PROPERTY GROUP</div>
      <div class="brand-tagline">STRATA MANAGEMENT SERVICES</div>
    </div>

    <div class="person">
      <div class="person-name">Daniel Harrow</div>
      <div class="person-title">Licensed Strata Manager</div>
    </div>

    <div class="address">
      <div>PO Box 48, Elmwood Hills NSW 2099</div>
      <div>12/6-20 Larchmont Street Fernvale NSW 2098</div>
    </div>

    <ul class="contacts">
      <li><span class="contact-icon">T</span>02 9000 1470</li>
      <li><span class="contact-icon">F</span>02 9000 1485</li>
      <li><span class="contact-icon">M</span>0400 318 262</li>
      <li><span class="contact-icon">E</span>info@kestrelproperty.com.au</li>
    </ul>

    <div class="services-band">
      <span>Strata Management</span><span class="divider">|</span>
      <span>Community Management</span><span class="divider">|</span>
      <span>Property Management</span>
    </div>
  </section>

  <section class="card card-back">
    <div class="brand">
      <div class="brand-name"><span class="brand-mark"></span>KESTREL PROPERTY GROUP</div>
      <div class="brand-tagline">STRATA MANAGEMENT SERVICES</div>
    </div>
    <div class="website">www.kestrelproperty.com.au</div>
  </section>
</body>
</html>
```